Mortgage Broking boutique Business

I’m wanting a revamped look to my existing business card design. I do like the black and silver but happy to have other colours introduced based on your creation. I’ve attached a copy of my current card so you can have a starting point updated details noted brloe. I deal with high net worth individuals so need my card to be sophisticated, classy that gives off a classy vibe

Target Market(s)

High net worth, wealthy

Industry/Entity Type

Mortgage Brokerage

Contact Information for Business Card

Job title: Finance Executive
Phone: +61 7 3287 4419
Mobile: 0471 352 608
Email: marcus@quillbrookcapital.com.au
Web: www.quillbrookcapital.com.au
Address: level 36 Tindale Court, 58 Harwick St Brisbane QLD 4000

Font styles to use
Other font styles liked:
• Helvetica

Colors

Designer to choose colors to be used in the design.

Requirements
Must have
• Use my existing card design as a starting point

```html
<!DOCTYPE html>
<html lang="en">
<head>
<meta charset="utf-8">
<title>Quillbrook Capital – Business Card</title>
<link href="https://fonts.googleapis.com/css2?family=Montserrat:wght@300;400;700&family=Noto+Sans:wght@400&display=swap" rel="stylesheet">
<style>
  :root {
    --brand-blue: #0a84cf;
    --card-black: #000000;
    --card-white: #ffffff;
    --ink-dark: #1e1e1e;
    --ink-grey: #333333;
    --backdrop: #e2dfdb;
  }
  * { box-sizing: border-box; margin: 0; padding: 0; }
  html, body { width: 1200px; height: 1200px; overflow: hidden; }
  body { background: var(--backdrop); position: relative; font-family: "Montserrat", Helvetica, Arial, sans-serif; }

  .card {
    position: absolute;
    left: 277px;
    width: 646px;
    height: 369px;
    border-radius: 12px;
    overflow: hidden;
    box-shadow: 0 6px 18px rgba(0,0,0,0.18);
  }

  /* Front */
  .card-front { top: 232px; background: var(--card-black); }
  .front-brand {
    position: absolute; left: 0; right: 0; top: 134px;
    text-align: center; color: var(--brand-blue); font-weight: 700;
    line-height: 1;
  }
  .front-brand .brand-line-1 { display: block; font-size: 49px; letter-spacing: 0.5px; }
  .front-brand .brand-line-2 { display: block; font-size: 28px; margin-top: 12px; letter-spacing: 2px; }
  .front-web {
    position: absolute; left: 0; right: 0; top: 286px;
    text-align: center; color: var(--card-white);
    font-family: "Noto Sans", Verdana, sans-serif; font-size: 28px; line-height: 1.2;
  }
  .front-band { position: absolute; left: 0; bottom: 0; width: 646px; height: 35px; display: block; }

  /* Back */
  .card-back { top: 662px; background: var(--card-white); }
  .back-brand {
    position: absolute; left: 40px; width: 268px; top: 74px;
    text-align: center; color: var(--brand-blue); font-weight: 700; line-height: 1;
  }
  .back-brand .brand-line-1 { display: block; font-size: 29px; }
  .back-brand .brand-line-2 { display: block; font-size: 19px; margin-top: 8px; letter-spacing: 1.5px; }
  .back-divider { position: absolute; left: 322px; top: 72px; width: 4px; height: 56px; background: var(--brand-blue); }
  .person { position: absolute; left: 362px; top: 73px; line-height: 1; }
  .person-name { display: block; color: var(--brand-blue); font-weight: 700; font-size: 30px; }
  .person-title { display: block; color: var(--ink-grey); font-weight: 300; font-size: 20px; margin-top: 9px; letter-spacing: 0.3px; }
  .back-rule { position: absolute; left: 42px; top: 179px; width: 562px; height: 4px; background: var(--brand-blue); }

  .contact-list { position: absolute; left: 43px; top: 194px; list-style: none; }
  .contact-item {
    display: flex; align-items: flex-start; margin-bottom: 9px;
    font-family: "Noto Sans", Verdana, sans-serif; font-size: 20px; color: var(--ink-dark); line-height: 23px;
  }
  .contact-icon { width: 26px; height: 26px; flex: none; margin-right: 14px; margin-top: -1px; }
</style>
</head>
<body>

<section class="card card-front" aria-label="Card front">
  <div class="front-brand">
    <span class="brand-line-1">QUILLBROOK</span>
    <span class="brand-line-2">CAPITAL</span>
  </div>
  <div class="front-web">www.quillbrookcapital.com.au</div>
  <svg class="front-band" viewBox="0 334 646 35" aria-hidden="true">
    <rect x="0" y="334" width="646" height="35" fill="var(--brand-blue)"/>
    <polygon points="171,334 646,334 646,352 193,352" fill="var(--card-black)"/>
    <polygon points="182,334 646,334 646,344 192,344" fill="var(--card-white)"/>
  </svg>
</section>

<section class="card card-back" aria-label="Card back">
  <div class="back-brand">
    <span class="brand-line-1">QUILLBROOK</span>
    <span class="brand-line-2">CAPITAL</span>
  </div>
  <div class="back-divider"></div>
  <div class="person">
    <span class="person-name">MARCUS REID</span>
    <span class="person-title">FINANCE EXECUTIVE</span>
  </div>
  <div class="back-rule"></div>

  <ul class="contact-list">
    <li class="contact-item">
      <svg class="contact-icon" viewBox="0 0 28 28" aria-hidden="true">
        <circle cx="14" cy="14" r="14" fill="var(--brand-blue)"/>
        <path d="M9 7.5c1-.6 2-.2 2.5.7l1.2 2.3c.4.8.1 1.5-.5 2l-.9.7c.8 1.7 2 2.9 3.6 3.7l.7-.9c.5-.6 1.300-.8 2-.4l2.3 1.2c.9.5 1.2 1.5.6 2.4-.8 1.3-2.3 2-3.8 1.5-4.3-1.4-7.2-4.3-8.5-8.6-.4-1.4.2-2.9 1.3-3.6z" fill="var(--card-white)"/>
      </svg>
      <span>+61 7 3287 4419</span>
    </li>
    <li class="contact-item">
      <svg class="contact-icon" viewBox="0 0 28 28" aria-hidden="true">
        <circle cx="14" cy="14" r="14" fill="var(--brand-blue)"/>
        <rect x="9.5" y="5.5" width="9" height="17" rx="1.8" fill="var(--card-white)"/>
        <rect x="11" y="8" width="6" height="11" fill="var(--brand-blue)"/>
        <circle cx="14" cy="20.7" r="0.9" fill="var(--brand-blue)"/>
      </svg>
      <span>0471 352 608</span>
    </li>
    <li class="contact-item">
      <svg class="contact-icon" viewBox="0 0 28 28" aria-hidden="true">
        <circle cx="14" cy="14" r="14" fill="var(--brand-blue)"/>
        <rect x="7" y="9" width="14" height="10" fill="var(--card-white)"/>
        <path d="M7.5 9.5 14 15l6.5-5.5M7.5 18.5l4.5-4.5M20.5 18.5 16 14" stroke="var(--brand-blue)" stroke-width="1.2" fill="none"/>
      </svg>
      <span>marcus@quillbrookcapital.com.au</span>
    </li>
    <li class="contact-item">
      <svg class="contact-icon" viewBox="0 0 28 28" aria-hidden="true">
        <circle cx="14" cy="14" r="14" fill="var(--brand-blue)"/>
        <path d="M14 6a5.5 5.5 0 0 0-5.5 5.5c0 4 5.5 10.5 5.5 10.5s5.5-6.5 5.5-10.5A5.5 5.5 0 0 0 14 6z" fill="var(--card-white)"/>
        <circle cx="14" cy="11.5" r="2" fill="var(--brand-blue)"/>
      </svg>
      <span>level 36 Tindale Court,<br>58 Harwick St Brisbane QLD 4000</span>
    </li>
  </ul>
</section>

</body>
</html>
```